Design a Chart Graphic that can be animated in video

We are looking for a clean and professional chart graphic that can be used on our website and edited to come alive in a video animation. The chart is to demonstrate that our product was proven to work in a clinical study. The chart title is Clinically Proven to Improve Sleep Quality. The x axis starts at "placebo" and ends at "tova calm" the placebo starts at 2% and the tova calm is 29% - the chart would show the rise from 2% to 29% in a dramatic way. The y axis would go from 0 - 30 %. There would be some sort of arrow to demonstrate the growth. Please see drawing for more clarity.

Target Market(s)

This is a study on SLEEP, the target market is sleep deprived men and women between the ages of 35-55.

Font styles to use
Sans Serif

Colors
0456a4
85abd2
85acd3
cedeed
ffffff
f04a50
fbed22

Requirements
Must have
• The chart must be delivered in a vector and styled in a way that can be animated by our video team. We are open to either flat or 3-D styles. The chart will be used on website and in video. It needs to look clean and professional, not funny or cartoonish. The color pallet needs to match www.itovacalm.com
• Please deliver vector, JPEG and PNG of the chart with and without a title.
Nice to have
• Fresh ideas to how to represent the chart in the most compelling way
Should not have
• Cartoons, gimmicky, colors other than those that match our website.

```html
<!DOCTYPE html>
<html lang="en">
<head>
<meta charset="utf-8">
<title>Sleep Quality Chart</title>
<link href="https://fonts.googleapis.com/css2?family=Open+Sans:wght@700&display=swap" rel="stylesheet">
<style>
  :root {
    --navy-panel: #1b3059;
    --navy-ink: #1b2a4e;
    --label-dark: #161c33;
    --white: #ffffff;
    --arrow-red: #e8000b;
    --bar-top-dark: #2d8fb5;
    --bar-top-light: #2180c4;
    --bar-mid-light: #2a94bc;
    --bar-fade-light: #e9eef1;
    --glow: #5fc8ff;
    --page: #ffffff;
  }
  html, body {
    margin: 0;
    padding: 0;
    width: 1034px;
    height: 1200px;
    overflow: hidden;
    background: var(--page);
  }
  .chart-sheet {
    display: block;
    width: 1034px;
    height: 1200px;
  }
  .axis-label {
    font-family: "Open Sans", sans-serif;
    font-weight: 700;
    font-size: 29px;
  }
  .axis-label--light { fill: var(--white); }
  .axis-label--dark { fill: var(--label-dark); }
  .axis-line--light { stroke: var(--white); stroke-width: 1.5; }
  .axis-line--dark { stroke: var(--label-dark); stroke-width: 1.5; }
  .panel-dark { fill: var(--navy-panel); }
  .growth-curve--red { fill: none; stroke: var(--arrow-red); stroke-width: 9; stroke-linecap: round; }
  .growth-head--red { fill: var(--arrow-red); }
  .growth-curve--navy { fill: none; stroke: var(--navy-ink); stroke-width: 12; stroke-linecap: round; }
  .growth-head--navy { fill: var(--navy-ink); }
</style>
</head>
<body>
<svg class="chart-sheet" viewBox="0 0 1772 2056" preserveAspectRatio="xMidYMid meet" xmlns="http://www.w3.org/2000/svg">
  <defs>
    <linearGradient id="bar-fill-dark" x1="0" y1="0" x2="0" y2="1">
      <stop offset="0" stop-color="var(--bar-top-dark)"/>
      <stop offset="1" stop-color="var(--navy-panel)"/>
    </linearGradient>
    <linearGradient id="bar-fill-light" x1="0" y1="0" x2="0" y2="1">
      <stop offset="0" stop-color="var(--bar-top-light)"/>
      <stop offset="0.35" stop-color="var(--bar-mid-light)"/>
      <stop offset="1" stop-color="var(--bar-fade-light)"/>
    </linearGradient>
    <radialGradient id="point-glow">
      <stop offset="0" stop-color="#ffffff"/>
      <stop offset="0.15" stop-color="var(--glow)"/>
      <stop offset="0.5" stop-color="#2f6fd0" stop-opacity="0.45"/>
      <stop offset="1" stop-color="#2f6fd0" stop-opacity="0"/>
    </radialGradient>
    <g id="growth-bars" transform="translate(-6,0)">
      <rect x="370" y="932" width="19" height="30"/>
      <rect x="398" y="928" width="19" height="34"/>
      <rect x="426" y="924" width="19" height="38"/>
      <rect x="455" y="919" width="19" height="43"/>
      <rect x="483" y="913" width="19" height="49"/>
      <rect x="511" y="907" width="19" height="55"/>
      <rect x="539" y="899" width="19" height="63"/>
      <rect x="567" y="892" width="19" height="70"/>
      <rect x="596" y="883" width="19" height="79"/>
      <rect x="624" y="874" width="19" height="88"/>
      <rect x="652" y="864" width="19" height="98"/>
      <rect x="680" y="853" width="19" height="109"/>
      <rect x="708" y="842" width="19" height="120"/>
      <rect x="736" y="830" width="19" height="132"/>
      <rect x="765" y="817" width="19" height="145"/>
      <rect x="793" y="804" width="19" height="158"/>
      <rect x="821" y="790" width="19" height="172"/>
      <rect x="849" y="775" width="19" height="187"/>
      <rect x="877" y="760" width="19" height="202"/>
      <rect x="906" y="744" width="19" height="218"/>
      <rect x="934" y="727" width="19" height="235"/>
      <rect x="962" y="710" width="19" height="252"/>
      <rect x="990" y="691" width="19" height="271"/>
      <rect x="1018" y="673" width="19" height="289"/>
      <rect x="1047" y="653" width="19" height="309"/>
      <rect x="1075" y="633" width="19" height="329"/>
      <rect x="1103" y="612" width="19" height="350"/>
      <rect x="1131" y="590" width="19" height="372"/>
      <rect x="1159" y="568" width="19" height="394"/>
      <rect x="1188" y="545" width="19" height="417"/>
      <rect x="1216" y="521" width="19" height="441"/>
      <rect x="1244" y="497" width="19" height="465"/>
      <rect x="1272" y="472" width="19" height="490"/>
      <rect x="1300" y="446" width="19" height="516"/>
      <rect x="1329" y="420" width="19" height="542"/>
      <rect x="1357" y="393" width="19" height="569"/>
      <rect x="1385" y="365" width="19" height="597"/>
    </g>
  </defs>

  <!-- Dark version -->
  <g class="chart chart--dark">
    <rect class="panel-dark" x="242" y="303" width="1279" height="762" rx="14"/>
    <use href="#growth-bars" fill="url(#bar-fill-dark)"/>
    <circle cx="370" cy="932" r="70" fill="url(#point-glow)"/>
    <circle cx="1388" cy="362" r="90" fill="url(#point-glow)"/>
    <line class="axis-line--light" x1="351" y1="355" x2="351" y2="975"/>
    <line class="axis-line--light" x1="351" y1="975" x2="1405" y2="975"/>
    <path class="growth-curve--red" d="M370 932 Q877.5 871.5 1382 370"/>
    <polygon class="growth-head--red" points="1402,338 1361,356 1390,383"/>
    <text class="axis-label axis-label--light" x="329" y="437" text-anchor="end">30%</text>
    <text class="axis-label axis-label--light" x="329" y="690" text-anchor="end">15%</text>
    <text class="axis-label axis-label--light" x="332" y="976" text-anchor="end">0%</text>
    <text class="axis-label axis-label--light" x="350" y="1017">Placebo</text>
    <text class="axis-label axis-label--light" x="1207" y="1017">TovaCalm</text>
  </g>

  <!-- Light version -->
  <g class="chart chart--light" transform="translate(-3,840)">
    <use href="#growth-bars" fill="url(#bar-fill-light)"/>
    <line class="axis-line--dark" x1="351" y1="355" x2="351" y2="975"/>
    <line class="axis-line--dark" x1="351" y1="975" x2="1405" y2="975"/>
    <path class="growth-curve--navy" d="M364 924 Q877.5 863 1380 365"/>
    <polygon class="growth-head--navy" points="1396,332 1356,348 1385,375"/>
    <text class="axis-label axis-label--dark" x="329" y="437" text-anchor="end">30%</text>
    <text class="axis-label axis-label--dark" x="329" y="690" text-anchor="end">15%</text>
    <text class="axis-label axis-label--dark" x="332" y="976" text-anchor="end">0%</text>
    <text class="axis-label axis-label--dark" x="350" y="1017">Placebo</text>
    <text class="axis-label axis-label--dark" x="1393" y="1017" text-anchor="end">TovaCalm</text>
  </g>
</svg>
</body>
</html>
```